Business Card Design

I am a classical pilates instructor. I have a home studio, teach out a of a large studio downtown, and teach at on location corporate settings
I like my card to be very simple and clean.
I would like a silhouette of the picture I'm uploading on my design. In the upload section it looks like the picture is cut off and only showing a leg in the air...let me know if you can open up the entire picture.

Industry/Entity Type
Business
Contact Information for Business Card
Norah Fennick Pilates
Certified - The Pilates Hall of Marrow Creek
nf.fennick27@quillpost.example
555.314.7720

```html
<!DOCTYPE html>
<html lang="en">
<head>
<meta charset="utf-8">
<title>Norah Fennick Pilates – Business Card</title>
<link href="https://fonts.googleapis.com/css2?family=Poiret+One&family=Open+Sans:wght@400;600&display=swap" rel="stylesheet">
<style>
  :root {
    --stage: #1c1c1c;
    --ink: #0e0e0e;
    --card-dark: #151515;
    --card-dark-2: #262626;
    --card-light: #f4f4f4;
    --card-mid: #bdbdbd;
    --rule: #d9d9d9;
    --text-dark: #1a1a1a;
    --text-light: #e6e6e6;
  }
  * { box-sizing: border-box; margin: 0; padding: 0; }
  html, body { width: 1200px; height: 1134px; overflow: hidden; }
  body {
    background: var(--stage);
    display: flex;
    flex-direction: column;
    align-items: center;
    justify-content: center;
    gap: 46px;
  }
  .card {
    position: relative;
    width: 900px;
    height: 514px;
    overflow: hidden;
    box-shadow: 0 14px 40px rgba(0,0,0,.6);
  }

  /* Back side */
  .card-back {
    background:
      repeating-linear-gradient(45deg, rgba(255,255,255,.025) 0 2px, transparent 2px 5px),
      radial-gradient(ellipse at 50% 40%, var(--card-dark-2), var(--card-dark) 75%);
  }
  .band {
    position: absolute;
    left: 0; right: 0;
    top: 205px;
    height: 104px;
    border-top: 2px solid var(--rule);
    border-bottom: 2px solid var(--rule);
    background: linear-gradient(180deg, #0b0b0b, #1a1a1a 50%, #0b0b0b);
    display: flex;
    align-items: center;
    justify-content: center;
  }
  .brand-name {
    font-family: "Poiret One", sans-serif;
    font-size: 52px;
    letter-spacing: 6px;
    color: var(--text-light);
    word-spacing: 14px;
  }

  /* Front side */
  .card-front {
    background: radial-gradient(ellipse at 62% 45%, var(--card-light) 0%, #d8d8d8 55%, var(--card-mid) 100%);
  }
  .front-curve { position: absolute; inset: 0; }
  .figure {
    position: absolute;
    left: 150px;
    top: 40px;
    width: 190px;
    height: 440px;
    border-radius: 40px;
    background: linear-gradient(180deg, #2a2a2a, #0a0a0a);
  }
  .divider {
    position: absolute;
    left: 440px;
    top: 110px;
    width: 6px;
    height: 250px;
    background: linear-gradient(90deg, rgba(0,0,0,.35), transparent);
    border-radius: 3px;
  }
  .details {
    position: absolute;
    left: 480px;
    top: 130px;
    color: var(--text-dark);
  }
  .details .name {
    font-family: "Poiret One", sans-serif;
    font-size: 44px;
    letter-spacing: 2px;
    line-height: 1.1;
  }
  .details .title {
    font-family: "Open Sans", sans-serif;
    font-size: 27px;
    letter-spacing: 1px;
    margin-top: 4px;
  }
  .details .studio {
    font-family: "Open Sans", sans-serif;
    font-size: 16px;
    margin-top: 4px;
  }
  .contact {
    list-style: none;
    margin-top: 40px;
    font-family: "Open Sans", sans-serif;
    font-size: 18px;
  }
  .contact li { display: flex; align-items: center; gap: 12px; margin-bottom: 8px; }
  .contact svg { width: 20px; height: 16px; fill: var(--text-dark); }
</style>
</head>
<body>

  <section class="card card-back">
    <div class="band">
      <span class="brand-name">Norah Fennick Pilates</span>
    </div>
  </section>

  <section class="card card-front">
    <svg class="front-curve" viewBox="0 0 900 514" preserveAspectRatio="none" aria-hidden="true">
      <path d="M0 0 H110 C180 140 210 360 150 514 H0 Z" fill="var(--ink)"/>
    </svg>
    <div class="figure" role="img" aria-label="Black silhouette of a pilates instructor holding an inverted pose"></div>
    <div class="divider"></div>
    <div class="details">
      <p class="name">Norah Fennick</p>
      <p class="title">Pilates Certified</p>
      <p class="studio">The Pilates Hall of Marrow Creek</p>
      <ul class="contact">
        <li>
          <svg viewBox="0 0 20 16" aria-hidden="true"><path d="M0 0h20v16H0z M1.5 1.5 10 9l8.5-7.5v13h-17z" fill-rule="evenodd"/></svg>
          nf.fennick27@quillpost.example
        </li>
        <li>
          <svg viewBox="0 0 20 16" aria-hidden="true"><path d="M1 4c0-2 2-3 9-3s9 1 9 3v2h-5V4H6v2H1z M4 8h12l2 7H2z"/></svg>
          555.314.7720
        </li>
      </ul>
    </div>
  </section>

</body>
</html>
```